Web Concept Design - modernize website

Looking to modernize our current website. http :// hvkwmaplebrook . com

Color Scheme: Use uploaded palette. (Black, Silver, Dark Purple, Greyish Blue)

The website needs to have a patient-friendly, community-friendly feel to it. While still being a professional medical website. We don't want it to have a cold, clinical feel.

Information on home page needs to be split into their own separate pages with designs for each.

Home Page:
Lantern Walk-In & Family Care is a family practice and urgent care clinic dedicated to providing high quality, compassionate health care, to patients of all ages.
Hours of operation:
Monday-Friday 9am-6:30pm
Saturday: CLOSED
Sunday: CLOSED
Primary Care visits will be by appointment only.
We will accept our last new patient at 6:00p and our last established patient at 6:30p.
We will no longer be doing DOT Physicals.

At bottom of home page:

Lantern Walk-In & Family Care understands that information about your health is private and we know how important it is to keep your medical information protected. We follow all HIPAA guidelines to protect the privacy of your medical records. The privacy act below explains our privacy practices and how we may use and disclose your medical information. If you would like for Lantern Walk-In & Family Care to release any or all of your medical information to others, you can make the request by signing a release and bring it with you at your next visit. If you would like to contact someone about the privacy and/or use of your medical information, you may contact us at 205-318-7602.

Click here for HIPAA document.

Click here for Medical Release form.

---------------

Services Page:
We provide family and urgent care for patients of all ages.

-Annual physicals
-Pre-employment drug screening
-Women's care including pap smears
-Screening and treatment for diabetes, hypertension and cholesterol
-All minor trauma such as abscesses, lacerations, burns and fractures
-Minor skin complaints
-Onsite LAB/XRAY/EKG
-Weight loss
-Adult and Pediatric Vaccinations
-Osteopathic manual medicine
-Medical pain management

-----

Payment & Insurance Page:
We now have online bill pay for patient balances. Please visit https://secure.paynestclinic.com/lwfc382pay to pay your bill today!

We currently accept all forms of insurance with the exception of Medicaid. Please bring a copy of your insurance card and photo ID upon visit. We are also a Veltrix prime provider. We do accept self-pay for patients who do not have insurance.

----

Meet Our Providers Page:

Dr. Stephen (Steve) Hadley, DO
Family Practice Physician

Professional Experience
April 4, 2010 to Present Lantern Walk-In & Family Care Owner
12 years of Emergency Medicine experience
6/1994 - 7/1997 NMI Birmingham, AL
Family Medicine Residency
10/1997 to Present Board Certified in Family Medicine
Recertified 2004
Education
9/1990 to 5/1994 Fairhaven Institute of Osteopathic Studies
Old Westbury, New York
Degree: Doctor of Osteopathic Medicine
9/1985 to 5/1989 Carrow-Lindell College
Birmingham, Alabama
Degree: Bachelor of Science
Membership
National Guild of Household Clinicians
Physicians Council of the Gulf Territory

----

Navigation Bar should have links for all the above pages + NEW PATIENTS + Access Your Medical Records (feel free to be creative with how you design this). We don't want the navigation bar to be too crowded.

Target Market(s)

Medical Patients

Number of Pages Required

5+ page

Colors

Designer to choose colors to be used in the design.

Requirements
Must have
• Designs for all pages
• Keep it professional
Nice to have
• Be creative!
Should not have
• No cold clinical, medical websites

```html
<!DOCTYPE html>
<html lang="en">
<head>
<meta charset="utf-8">
<title>Lantern Walk-In & Family Care</title>
<link href="https://fonts.googleapis.com/css2?family=Josefin+Sans:wght@300;400;600;700&family=Tinos:ital,wght@0,400;0,700;1,400;1,700&display=swap" rel="stylesheet">
<style>
:root{
  --purple:#7c4a80;
  --purple-soft:#a47aa8;
  --ink:#231f20;
  --grey:#6f6a70;
  --silver:#c9c7cc;
  --card:#f3f3f7;
  --white:#ffffff;
}
*{margin:0;padding:0;box-sizing:border-box}
html,body{width:1200px;height:3232px;overflow:hidden;background:var(--white)}
body{position:relative;font-family:"Josefin Sans",sans-serif;color:var(--ink)}
.abs{position:absolute}
.btn{position:absolute;display:flex;align-items:center;justify-content:center;border-radius:20px;font-size:12px;font-weight:600;letter-spacing:.2px}
.btn-outline{border:1.5px solid var(--purple);color:var(--purple)}
.btn-solid{background:var(--purple);color:var(--white)}

/* header */
.logo{left:152px;top:14px;width:190px;font-family:"Tinos",serif;font-size:19px;line-height:23px;color:var(--purple)}
.logo .second{display:block;padding-left:92px}
.contact{display:flex;align-items:center;gap:12px;top:16px}
.contact .dot{width:34px;height:34px;border-radius:50%;background:var(--purple);display:flex;align-items:center;justify-content:center}
.contact .phone-dot{background:var(--white);border:1.5px solid var(--silver)}
.contact b{display:block;font-family:"Tinos",serif;font-size:14px}
.contact span{font-size:13px;color:var(--grey)}
.nav{left:0;top:80px;width:1200px;height:42px;background:var(--ink)}
.nav ul{list-style:none;display:flex;justify-content:space-between;position:absolute;left:152px;top:0;width:886px;height:42px}
.nav li{color:var(--white);font-size:13.5px;padding:0 18px;line-height:44px}
.nav li:last-child{padding-right:8px}
.nav li.active{background:var(--purple)}

/* hero */
.hero{left:0;top:122px;width:1200px;height:530px;background:linear-gradient(100deg,#eef0f1 0%,#e3e6e4 40%,#c9cfc4 70%,#8f9d7c 100%)}
.hero-kicker{left:152px;top:268px;font-family:"Tinos",serif;font-style:italic;font-weight:700;font-size:22px;color:var(--ink)}
.hero-kicker em{color:var(--purple)}
.hero-title{left:152px;top:300px;font-family:"Tinos",serif;font-weight:700;font-size:38px;line-height:47px;color:var(--ink)}
.hero-title span{color:var(--purple)}
.dots{left:152px;top:592px;display:flex;gap:8px}
.dots i{display:block;width:40px;height:2px;background:var(--white)}
.dots i.on{background:var(--purple)}

/* welcome */
.eyebrow{font-size:11px;font-weight:600;color:var(--ink)}
.welcome-copy{left:230px;top:718px;width:380px}
.welcome-copy h2{font-family:"Tinos",serif;font-weight:400;font-size:28px;margin-top:6px}
.welcome-copy h2 span{color:var(--purple)}
.welcome-copy p{width:360px;font-size:14.5px;line-height:23px;color:var(--grey);margin-top:20px}
.welcome-copy h4{font-family:"Tinos",serif;font-size:19px;margin-top:30px}
.hours{font-size:17px;line-height:30px;color:var(--grey);margin-top:24px}
.hours b{color:var(--ink);font-weight:600}
.hours em{font-style:normal;color:var(--purple)}
.welcome-photo{left:689px;top:652px;width:281px;height:483px;background:linear-gradient(160deg,#e9e6ea,#cfc7cf 60%,#b9b0b9)}

/* services */
.services{left:0;top:1135px;width:1200px;height:485px;background:var(--purple)}
.services-photo{left:152px;top:1135px;width:283px;height:485px;background:linear-gradient(170deg,#dcdfe2,#b9bfc5 55%,#8a8d95)}
.services-copy{left:510px;top:1196px;color:var(--white)}
.services-copy .eyebrow{color:var(--white)}
.services-copy h2{font-family:"Tinos",serif;font-weight:400;font-size:28px;margin-top:6px}
.services-copy p{font-size:17px;margin-top:18px}
.svc{position:absolute;display:flex;align-items:center;gap:8px;font-size:13px;color:var(--white);font-weight:600}

/* payment */
.payment{left:0;top:1680px;width:1200px;text-align:center}
.payment h2{font-family:"Tinos",serif;font-weight:400;font-size:28px;margin-top:6px}
.payment h2 span{color:var(--purple)}
.payment p{font-size:21px;color:var(--grey);margin-top:8px}

/* about */
.about{left:0;top:1895px;width:1200px;height:442px;background:var(--ink)}
.about-copy{left:152px;top:1960px;width:830px;color:var(--white)}
.about-copy .eyebrow{color:var(--white)}
.about-copy h2{font-family:"Tinos",serif;font-weight:400;font-size:28px;margin-top:6px}
.about-copy p{font-size:13px;line-height:19.5px;color:#a9a5aa;margin-top:14px}
.about-copy p b{color:var(--purple-soft)}

/* provider */
.provider-photo{left:152px;top:2288px;width:359px;height:475px;background:linear-gradient(160deg,#e4e6e8,#c4c8cc 55%,#9fa4aa)}
.provider-card{left:511px;top:2288px;width:537px;height:475px;background:var(--card);box-shadow:0 10px 30px rgba(0,0,0,.08)}
.provider-inner{position:absolute;left:48px;top:52px;width:440px}
.provider-inner h2{font-family:"Tinos",serif;font-weight:400;font-size:28px;color:var(--purple);margin-top:8px}
.provider-inner h2 span{color:var(--ink)}
.role{font-size:11.5px;border-top:1px solid var(--silver);border-bottom:1px solid var(--silver);padding:14px 0;margin-top:10px}
.provider-inner h4{font-family:"Tinos",serif;font-size:19px;margin-top:26px}
.exp-date{font-size:12.5px;font-weight:600;margin-top:18px}
.exp-line{font-size:12.5px;color:var(--grey);margin-top:12px}

/* footer */
.map{left:0;top:2714px;width:511px;height:453px;background:linear-gradient(135deg,#f0f0f1,#e2e2e4)}
.footer{left:511px;top:2714px;width:689px;height:453px;background:var(--ink);color:var(--white)}
.footer h4{position:absolute;font-family:"Tinos",serif;font-size:18px}
.footer .txt{position:absolute;font-size:13.5px;line-height:19px;color:#bdb9bd}
.footer .hl{color:var(--purple-soft)}
.rule-v{position:absolute;left:278px;top:46px;width:1px;height:360px;background:#4a4547}
.rule-h{position:absolute;height:1px;background:#4a4547}
.social{position:absolute;left:338px;top:331px;display:flex;gap:10px}
.social i{display:block;width:30px;height:30px;border-radius:50%;background:#d0ccd0}
.social i.on{background:var(--purple)}
.copyright{left:152px;top:3167px;width:896px;height:65px;background:var(--purple);color:var(--white);font-size:13px;line-height:65px;padding-left:30px}
.copyright u{text-underline-offset:2px}
.to-top{position:absolute;right:80px;top:23px;width:22px;height:22px;border-radius:50%;background:var(--ink)}
</style>
</head>
<body>

<!-- header -->
<div class="abs logo">Lantern Walk-In &amp;<span class="second">Family Care</span></div>
<div class="abs contact" style="left:460px">
  <div class="dot"><svg width="16" height="12" viewBox="0 0 16 12"><rect x="1" y="1" width="14" height="10" fill="none" stroke="#fff" stroke-width="1.5"/><path d="M1 1l7 6 7-6" fill="none" stroke="#fff" stroke-width="1.5"/></svg></div>
  <div><b>Email Us:</b><span style="text-decoration:underline">hello@lanternwalkin.care</span></div>
</div>
<div class="abs contact" style="left:712px">
  <div class="dot phone-dot"><svg width="14" height="14" viewBox="0 0 14 14"><path d="M3 1l2 3-1.5 1.5c1 2 2.5 3.5 4.5 4.5L9.5 8.5l3 2-1 2.5C6 13 1 8 1 2.5z" fill="var(--ink)"/></svg></div>
  <div><b>Call Us:</b><span>205.318.7602</span></div>
</div>
<div class="btn btn-solid" style="left:893px;top:19px;width:153px;height:35px;font-size:12.5px">Book Appointment</div>

<nav class="abs nav">
  <ul>
    <li class="active">Home</li><li>Services</li><li>Payment &amp; Insurance</li><li>Meet Our Providers</li><li>New Patients</li><li>Access Your Medical Records</li>
  </ul>
</nav>

<!-- hero -->
<div class="abs hero" role="img" aria-label="Photo of a smiling mother and young daughter playing outdoors in sunlight"></div>
<div class="abs hero-kicker"><em>Lantern Walk-In</em> &amp; Family Care</div>
<h1 class="abs hero-title">is a <span>Family Practice</span> and<br><span>Urgent Care</span> Clinic</h1>
<div class="btn btn-outline" style="left:152px;top:417px;width:130px;height:32px">Contact Us</div>
<div class="abs dots"><i></i><i class="on"></i><i></i></div>

<!-- welcome -->
<section class="abs welcome-copy">
  <div class="eyebrow">Welcome to</div>
  <h2><span>Lantern Walk-In</span> &amp; Family Care</h2>
  <p>Is a family practice and urgent care clinic dedicated to providing high quality, compassionate health care, to patients of all ages.</p>
  <h4>Hours of Operation:</h4>
  <div class="hours">Monday - Friday: <b>9am-6:30pm</b><br>Saturday - Sunday: <em>Closed</em></div>
</section>
<div class="btn btn-outline" style="left:230px;top:1040px;width:130px;height:32px">Contact Us</div>
<div class="abs welcome-photo" role="img" aria-label="Photo of a doctor examining a young girl with her mother"></div>

<!-- services -->
<div class="abs services"></div>
<div class="abs services-photo" role="img" aria-label="Photo of a doctor taking a patient's blood pressure"></div>
<section class="abs services-copy">
  <div class="eyebrow">What We Do</div>
  <h2>Our Services</h2>
  <p>We provide family and urgent care for patients of all ages.</p>
</section>
<svg width="0" height="0" style="position:absolute"><defs><symbol id="tick" viewBox="0 0 12 12"><rect x=".75" y=".75" width="10.5" height="10.5" fill="none" stroke="#fff" stroke-width="1.3"/><path d="M3 6l2.2 2.2L9.5 3.5" fill="none" stroke="#fff" stroke-width="1.5"/></symbol></defs></svg>
<div class="svc" style="left:510px;top:1320px"><svg width="12" height="12"><use href="#tick"/></svg>Annual physicals</div>
<div class="svc" style="left:510px;top:1351px"><svg width="12" height="12"><use href="#tick"/></svg>Pre-employment drug screening</div>
<div class="svc" style="left:510px;top:1382px"><svg width="12" height="12"><use href="#tick"/></svg>Women's care including pap smears</div>
<div class="svc" style="left:510px;top:1413px"><svg width="12" height="12"><use href="#tick"/></svg>Screening and treatment for diabetes, hypertension and cholesterol</div>
<div class="svc" style="left:510px;top:1444px"><svg width="12" height="12"><use href="#tick"/></svg>All minor trauma such as abscesses, lacerations, burns and fractures</div>
<div class="svc" style="left:510px;top:1475px"><svg width="12" height="12"><use href="#tick"/></svg>Minor skin complaints</div>
<div class="svc" style="left:510px;top:1506px"><svg width="12" height="12"><use href="#tick"/></svg>Weight loss</div>
<div class="svc" style="left:510px;top:1537px"><svg width="12" height="12"><use href="#tick"/></svg>Osteopathic manual medicine</div>
<div class="svc" style="left:802px;top:1475px"><svg width="12" height="12"><use href="#tick"/></svg>Onsite LAB/XRAY/EKG</div>
<div class="svc" style="left:802px;top:1506px"><svg width="12" height="12"><use href="#tick"/></svg>Adult and Pediatric Vaccinations</div>
<div class="svc" style="left:802px;top:1537px"><svg width="12" height="12"><use href="#tick"/></svg>Medical pain management</div>

<!-- payment -->
<section class="abs payment">
  <div class="eyebrow">Online Bill Pay</div>
  <h2><span>Payment</span> &amp; Insurance</h2>
  <p>We now have online bill pay for patient balances.</p>
</section>
<div class="btn btn-solid" style="left:511px;top:1800px;width:178px;height:32px">Pay Your Bill Today!</div>

<!-- about -->
<div class="abs about"></div>
<section class="abs about-copy">
  <div class="eyebrow">About Us</div>
  <h2>Lantern Walk-In &amp; Family Care</h2>
  <p>Understands that information about your health is private and we know how important it is to keep your medical information protected. We follow all HIPAA guidelines to protect the privacy of your medical records.</p>
  <p>The privacy act below explains our privacy practices and how we may use and disclose your medical information. If you would like for Lantern Walk-In &amp; Family Care to release any or all of your medical information to others, you can make the request by signing a release and bring it with you at your next visit. If you would like to contact someone about the privacy and/or use of your medical information, you may <b>contact us at 205-318-7602.</b></p>
</section>
<div class="btn btn-outline" style="left:152px;top:2189px;width:282px;height:33px;border-color:#5a555a;color:var(--purple-soft)">Click Here for HIPAA Document</div>
<div class="btn btn-solid" style="left:451px;top:2189px;width:282px;height:33px">Click Here for Medical Release form</div>

<!-- provider -->
<div class="abs provider-photo" role="img" aria-label="Portrait photo of the family practice physician in a white coat"></div>
<section class="abs provider-card">
  <div class="provider-inner">
    <div class="eyebrow" style="color:var(--grey)">Our Providers</div>
    <h2>Dr. Stephen <span>(Steve) Hadley,</span></h2>
    <div class="role">Family Practice Physician</div>
    <h4>Professional Experience:</h4>
    <div class="exp-date">April 4, 2010 to Present</div>
    <div class="exp-line">Lantern Walk-In &amp; Family Care Owner</div>
    <div class="exp-line" style="margin-top:20px">12 years of Emergency Medicine experience</div>
    <div class="exp-date" style="margin-top:24px">6/1994 - 7/1997</div>
    <div class="exp-line">NMI Birmingham, AL Family Medicine Residency</div>
  </div>
</section>
<div class="btn btn-outline" style="left:559px;top:2677px;width:112px;height:31px">More Info!</div>

<!-- footer -->
<div class="abs map" role="img" aria-label="Street map showing the clinic location with a pin"></div>
<svg class="abs" style="left:245px;top:2920px" width="22" height="30" viewBox="0 0 22 30"><path d="M11 1C5.5 1 1 5.3 1 10.8 1 18 11 29 11 29s10-11 10-18.2C21 5.3 16.5 1 11 1z" fill="var(--purple)"/><circle cx="11" cy="11" r="4" fill="#fff"/></svg>
<footer class="abs footer">
  <h4 style="left:48px;top:108px">Address</h4>
  <div class="txt" style="left:48px;top:150px;width:200px">2180 Maple Brook<br>Road Suite 204 Maplebrook,<br>AL 35190</div>
  <div class="txt hl" style="left:48px;top:224px;font-size:12px;text-decoration:underline">→&nbsp; Get Direction</div>
  <div class="rule-h" style="left:48px;top:266px;width:200px"></div>
  <h4 style="left:48px;top:294px">Contact Us</h4>
  <div class="txt" style="left:48px;top:334px"><span class="hl">Phone:</span> 205.318.7602<br><span class="hl">Fax:</span> 205.471.2290<br><span style="text-decoration:underline">hello@lanternwalkin.care</span></div>
  <div class="rule-v"></div>
  <h4 style="left:338px;top:108px">Hours of Operation</h4>
  <div class="txt" style="left:338px;top:150px"><span class="hl">Monday - Friday</span><br>9am-6:30pm<br><br><span class="hl">Saturday - Sunday</span><br>Closed</div>
  <div class="rule-h" style="left:338px;top:266px;width:200px"></div>
  <h4 style="left:338px;top:294px">Get Social</h4>
  <div class="social"><i></i><i class="on"></i><i></i><i></i></div>
</footer>
<div class="abs copyright">©2018 <u>Lantern Walk-In and Family Care</u>. All rights reserved.<span class="to-top"></span></div>

</body>
</html>
```